Flyer promoting Velmora's workshops and credentials

We run Training workshops for the data analyst community. We'd like a flyer to sell our services using a style and colour scheme consistent with our website www.velmoraskills.co.uk . I've attached some background info and some existing e-brochures for different workshops to give a flavour for content (but these are poorly designed and we don't want a similar design!!). There's also an overview document which gives more direction. The flyer will be sent with an accompanying letter to Learning & Development decision makers as well as Anlaytical team managers. It's purpose would be to generate enquiries and bookings for primarliy our flagship workshop 'Turning Figures Into Real Results'.

Target Market(s)

Learning and Development senior managers
Analytical team managers

Industry/Entity Type

Training

Font styles to use
Other font styles liked:
• Similar to website for consistency

Requirements
Must have
• Good copy! Slick design more in line with European (UK) style advertising rather than US.
Nice to have
• Some humour,
Should not have
• should not be as boring and non-sales based as the website!! Website is not a great example!

```html
<!DOCTYPE html>
<html lang="en">
<head>
<meta charset="utf-8">
<title>Velmora – Workshops &amp; Seminars</title>
<link href="https://fonts.googleapis.com/css2?family=Arimo:ital,wght@0,400;0,700;1,400&display=swap" rel="stylesheet">
<style>
  :root {
    --navy: #2b4f86;
    --navy-dark: #1c2a40;
    --orange: #f7941d;
    --ink: #222;
    --muted: #555;
    --grey: #9a9a9a;
    --box-blue: #d1d6e7;
    --box-cream: #fdf0e2;
    --white: #fff;
  }
  * { margin: 0; padding: 0; box-sizing: border-box; }
  html, body { width: 849px; height: 1200px; overflow: hidden; background: var(--white); }
  body { font-family: "Arimo", Arial, sans-serif; color: var(--ink); position: relative; }

  .brand { position: absolute; left: 42px; top: 36px; }
  .brand-name { display: flex; align-items: center; gap: 8px; font-size: 50px; font-weight: 700; color: var(--navy); line-height: 1; letter-spacing: -1px; }
  .brand-dot { width: 14px; height: 14px; border-radius: 50%; background: var(--orange); }
  .brand-tagline { margin: 6px 0 0 74px; font-size: 16px; font-weight: 700; color: var(--orange); }

  .site-url { position: absolute; right: 46px; top: 40px; font-size: 16px; letter-spacing: 2.6px; color: #333; }

  .title-band { position: absolute; left: 0; top: 128px; width: 849px; height: 84px;
    background: linear-gradient(90deg, var(--navy-dark) 0%, #22385a 45%, #24477c 100%);
    border-bottom: 4px solid var(--orange); }
  .title-band h1 { position: absolute; left: 42px; top: 28px; font-size: 40px; font-weight: 700; color: var(--white); }

  .hero-photo { position: absolute; left: 548px; top: 88px; width: 258px; height: 213px;
    background: linear-gradient(135deg, #d9d3cb 0%, #eef1f4 45%, #b9c6d6 100%);
    box-shadow: 0 6px 10px rgba(0,0,0,0.15); }

  .intro { position: absolute; left: 42px; top: 236px; width: 460px; font-size: 17px; line-height: 23.6px; }

  .column-rule { position: absolute; left: 525px; top: 236px; width: 1px; height: 876px; background: #8a8a8a; }

  .workshop { position: absolute; left: 28px; width: 485px; padding: 14px 14px 0 14px; }
  .workshop.blue { background: var(--box-blue); }
  .workshop.cream { background: var(--box-cream); }
  .workshop h2 { font-size: 17px; font-weight: 700; text-transform: uppercase; line-height: 22px; margin-top: 2px; }
  .workshop.blue h2 { color: var(--navy); }
  .workshop.cream h2 { color: var(--orange); }
  .workshop p { margin-top: 12px; font-size: 15.3px; line-height: 21.7px; color: #333; }
  .duration { position: absolute; right: 8px; top: 8px; height: 28px; padding: 0 8px 0 20px;
    font-size: 17px; font-weight: 700; color: var(--white); line-height: 28px;
    clip-path: polygon(0 0, 100% 0, 100% 100%, 0 100%, 7px 50%); }
  .blue .duration { background: var(--navy); }
  .cream .duration { background: var(--orange); }

  .testimonials-heading { position: absolute; left: 549px; top: 330px; font-size: 22px; font-style: italic; letter-spacing: 9px; color: var(--grey); white-space: nowrap; }
  .testimonial { position: absolute; left: 551px; width: 256px; font-size: 13.4px; line-height: 18.8px; }
  .testimonial q { display: block; font-style: italic; color: var(--muted); quotes: none; letter-spacing: -0.1px; }
  .testimonial cite { display: block; font-style: normal; font-size: 14px; text-align: right; margin-top: 4px; color: #222; line-height: 18.5px; }
  .testimonial-rule { position: absolute; left: 551px; width: 254px; height: 3px; background: var(--orange); }

  .footer-rule { position: absolute; left: 27px; top: 1135px; width: 795px; height: 2px; background: var(--navy); }
  .footer { position: absolute; left: 42px; top: 1148px; width: 763px; display: flex; align-items: center; justify-content: space-between; font-size: 14px; color: #333; }
  .footer .company { font-size: 17px; color: var(--navy); }
  .footer .sep { width: 1px; height: 18px; background: #333; }
</style>
</head>
<body>
  <header class="brand">
    <div class="brand-name"><span>Velmora</span><span class="brand-dot"></span></div>
    <div class="brand-tagline">Workshops for Data Analysts</div>
  </header>
  <div class="site-url">www.velmoraskills.co.uk</div>

  <div class="title-band"><h1>Workshops &amp; Seminars</h1></div>
  <div class="hero-photo" role="img" aria-label="Photo of colleagues pointing at charts on a tablet over printed reports"></div>

  <p class="intro">Velmora's workshops are interactive and practical. Delegates can attend one of the scheduled public workshops or if you have several analysts, an on-site private workshop offers significant savings and the chance to work through challenges as a team.</p>

  <div class="column-rule"></div>

  <section class="workshop blue" style="top:374px;height:144px">
    <h2>Turning Figures Into Real Results</h2>
    <span class="duration">2 Days</span>
    <p>A CPD accredited, interactive soft-skills workshop to improve the productivity and impact an analyst has on the organisation they support. Focusing on the three core themes of Communication, Presentation of Data and Planning.</p>
  </section>

  <section class="workshop cream" style="top:529px;height:126px">
    <h2>Delivering Analysis for Impact</h2>
    <span class="duration">.5 Day</span>
    <p>A half day seminar on the key behaviours and techniques information analysts/insight specialists need to employ in order to have a positive impact on their internal or external customers.</p>
  </section>

  <section class="workshop blue" style="top:666px;height:142px">
    <h2>Influencing Skills</h2>
    <span class="duration">1 Day</span>
    <p>This workshop equips the analyst with a set of established techniques and principals to help them effectively influence their customers and internal decision makers - a key skill to ensuring personal and commercials goals are achieved.</p>
  </section>

  <section class="workshop cream" style="top:818px;height:142px">
    <h2>Analytics in Direct Marketing</h2>
    <span class="duration">1 Day</span>
    <p>A workshop to help delegates understand the tactical and strategic analytics which support the direct marketing life cycle. Includes practical exercises to reinforce the learnings. This workshop can only be hosted privately.</p>
  </section>

  <section class="workshop blue" style="top:969px;height:143px">
    <h2>Tailored Statistical Workshops</h2>
    <span class="duration">1 Day</span>
    <p>Customisable workshops - select the statistical methods and techniques you and your colleagues would like to cover and we'll provide you with a tailored day with practical examples and accompanying notes.</p>
  </section>

  <aside class="testimonials">
    <div class="testimonials-heading">‘TESTIMONIALS’</div>

    <div class="testimonial" style="top:368px">
      <q>“We took from the course a number of actionable learnings that we have put into practice and this has resulted in positive feedback and a happier more valued team. Recommend the course to new and experienced analysts alike.”</q>
      <cite>— Tom Harker, Brightwell Aid</cite>
    </div>
    <div class="testimonial-rule" style="top:521px"></div>

    <div class="testimonial" style="top:541px">
      <q>“Turning Figures Into Real Results is a high quality, well-structured course delivered by a skilled and knowledgeable trainer. It has provided our analysts with the invaluable customer-focussed skills and techniques that have added value to the whole of the marketing process and a new and original dimension to the career development of our analysis teams."</q>
      <cite>— Daniel Moss, Northgate Mutual Finance</cite>
    </div>
    <div class="testimonial-rule" style="top:764px"></div>

    <div class="testimonial" style="top:786px">
      <q>“I really enjoyed the session. It was pitched well for the skill set of attendees. I got a lot out of it in respect of tables/visuals formatting and have totally re-thought my initial views of providing/producing data for my customers. Thankyou."</q>
      <cite>— Claire Pennant, Arvion Systems</cite>
    </div>
    <div class="testimonial-rule" style="top:955px"></div>

    <div class="testimonial" style="top:979px">
      <q>“Excellent &amp; relevant exercises. All exercise solutions supplied so no need to worry about interpreting scribbled calculations. Pace good and good help available when stuck. Covered all areas I was expecting."</q>
      <cite>— Nadia Fairley, Brightwell Aid</cite>
    </div>
  </aside>

  <div class="footer-rule"></div>
  <footer class="footer">
    <span class="company">Velmora Skills Ltd</span>
    <span class="sep"></span>
    <span>Tel: 0161 555 0142</span>
    <span class="sep"></span>
    <span>Fax: 0845 5550178</span>
    <span class="sep"></span>
    <span>Email: hello@velmoraskills.co.uk</span>
  </footer>
</body>
</html>
```